Bright Lanterns Business Card

Design of business cards

Target Market(s)

We are aiming as small business owners who need anything from basic business structures, website plans, business processes and quality assurance.

Industry/Entity Type

Business

Colors

Designer to choose colors to be used in the design.

Requirements
Nice to have
• I would prefer one side of the card to use the green from the logo. Prefer to have the same font as the logo.

```html
<!DOCTYPE html>
<html lang="en">
<head>
<meta charset="utf-8">
<title>Bright Lanterns Consulting – Business Card</title>
<link rel="stylesheet" href="https://fonts.googleapis.com/css2?family=Crimson+Pro:wght@400;600;700&display=swap">
<style>
  :root {
    --lantern-green: #a6ce39;
    --slate: #5b5b5d;
    --paper: #ffffff;
  }
  * { margin: 0; padding: 0; box-sizing: border-box; }
  html, body {
    width: 1200px;
    height: 741px;
    overflow: hidden;
    background: var(--paper);
  }
  .card {
    position: relative;
    width: 1200px;
    height: 741px;
    background: var(--paper);
    font-family: "Crimson Pro", Georgia, serif;
    color: var(--slate);
  }
  .band-top {
    position: absolute;
    left: 0; top: 0;
    width: 100%; height: 77px;
    background: var(--lantern-green);
  }
  .band-bottom {
    position: absolute;
    left: 0; top: 502px;
    width: 100%; height: 239px;
    background: var(--lantern-green);
  }
  .rule {
    position: absolute;
    left: 0;
    width: 410px;
    height: 2px;
    background: var(--slate);
  }
  .rule--contact { top: 149px; }
  .rule--services { top: 619px; }
  .contact {
    position: absolute;
    left: 429px;
    top: 119px;
    height: 65px;
    display: flex;
    align-items: flex-start;
    font-size: 38px;
    line-height: 1;
  }
  .contact__name {
    font-weight: 700;
    padding-top: 12px;
    padding-right: 16px;
    letter-spacing: 0.3px;
  }
  .contact__divider {
    width: 1px;
    height: 65px;
    background: var(--slate);
  }
  .contact__phone {
    font-weight: 400;
    padding-top: 12px;
    padding-left: 16px;
  }
  .brand {
    position: absolute;
    left: 36px;
    top: 335px;
    display: flex;
    align-items: center;
    gap: 48px;
  }
  .brand__mark {
    width: 150px;
    height: 150px;
    border-radius: 50%;
    background: var(--lantern-green);
  }
  .brand__name {
    font-weight: 600;
    font-size: 52px;
    line-height: 58px;
    text-transform: uppercase;
    letter-spacing: 1px;
    color: var(--slate);
  }
  .services {
    position: absolute;
    left: 430px;
    top: 584px;
    font-size: 26px;
    line-height: 34px;
    font-weight: 400;
    color: var(--slate);
  }
</style>
</head>
<body>
  <div class="card">
    <div class="band-top"></div>

    <div class="rule rule--contact"></div>
    <div class="contact">
      <span class="contact__name">Marco Velentini</span>
      <span class="contact__divider"></span>
      <span class="contact__phone">555.201.4836</span>
    </div>

    <div class="brand">
      <div class="brand__mark"></div>
      <div class="brand__name">Bright<br>Lanterns<br>Consulting</div>
    </div>

    <div class="band-bottom"></div>
    <div class="rule rule--services"></div>
    <p class="services">basic business structures, website plans,<br>business processes &amp; quality assurance</p>
  </div>
</body>
</html>
```